Dental Office Looking for Modern, simple business cards

We just acquired our logo. Now we would like to make business cards. We are a dental office with two doctors. We are husband and wife and have a small boutique dental practice in a small town. We love our patients and they are always asking us to give our business cards to their friends. Please help us make business cards :-)

Target Market(s)

30-60 yr old

Industry/Entity Type

Dental Clinic

Contact Information for Business Card

Birch Hollow Dental P.C.
Family and Cosmetic Dentistry
4826 Delmore Rd. Schenectady NY 12417
Tel: 518 642 7731 Fax: 518 642 7048

Dr. Tomas K. Brellin DDS
Dr. Marisol Ede Thornquist DDS

Font styles to use
Serif
Sans Serif

Requirements
Must have
• Simple clean design, modern, colorful. Should incorporate the logo.
Nice to have
• dental imagery ( teeth, smile, etc ...).

```html
<!DOCTYPE html>
<html lang="en">
<head>
<meta charset="utf-8">
<title>Birch Hollow Dental – Business Cards</title>
<link rel="stylesheet" href="https://fonts.googleapis.com/css2?family=Exo+2:wght@600;700&family=Open+Sans:wght@400;600&display=swap">
<style>
  :root {
    --bg: #e9eaec;
    --card: #ffffff;
    --blue: #1f73c4;
    --blue-deep: #1563ad;
    --blue-light: #3f8fd6;
    --grey-text: #6d7075;
    --grey-rule: #9a9da2;
    --dash: #4a8fd4;
    --skin-light: #f3d9d6;
    --skin-mid: #e8bdb8;
    --lip: #d98e96;
  }
  * { box-sizing: border-box; margin: 0; padding: 0; }
  html, body {
    width: 1200px; height: 900px; overflow: hidden;
    background: var(--bg);
    font-family: "Open Sans", Arial, sans-serif;
  }
  .sheet {
    width: 1200px; height: 900px;
    display: flex; flex-direction: column;
    align-items: center; justify-content: center; gap: 30px;
  }
  .card {
    position: relative;
    width: 720px; height: 411px;
    background: var(--card);
    overflow: hidden;
    box-shadow: 0 2px 10px rgba(0,0,0,.12);
  }

  /* Back side */
  .card-back__band {
    height: 118px;
    background: linear-gradient(90deg, var(--blue-deep), var(--blue-light));
    display: flex; align-items: center; justify-content: center;
  }
  .wordmark {
    font-family: "Exo 2", Arial, sans-serif;
    font-weight: 700;
    letter-spacing: 1px;
    text-transform: uppercase;
    display: flex; align-items: center; gap: 10px;
  }
  .wordmark__dot {
    width: 14px; height: 14px; border-radius: 50%;
    background: currentColor;
  }
  .card-back .wordmark { color: #ffffff; font-size: 30px; }
  .appointment-lines {
    padding: 62px 70px 0 150px;
    display: flex; flex-direction: column; gap: 56px;
  }
  .appointment-lines span {
    display: block;
    border-top: 2px dashed var(--dash);
  }

  /* Front side */
  .card-front__photo {
    position: absolute; left: 0; top: 0; bottom: 0;
    width: 400px;
    background:
      linear-gradient(90deg, rgba(255,255,255,0) 55%, #ffffff 100%),
      radial-gradient(ellipse 60% 22% at 45% 62%, var(--lip) 0%, rgba(217,142,150,0) 100%),
      linear-gradient(160deg, var(--skin-light), var(--skin-mid));
  }
  .card-front__info {
    position: absolute; left: 390px; top: 54px; right: 36px;
  }
  .card-front .wordmark { color: var(--blue); font-size: 30px; }
  .wordmark-rule {
    width: 270px; height: 2px; margin-top: 10px;
    background: var(--grey-rule);
  }
  .doctor {
    margin-top: 30px;
    font-family: "Exo 2", Arial, sans-serif;
    font-weight: 700; font-size: 20px;
    color: var(--blue);
  }
  .specialty {
    font-size: 15px; color: var(--grey-text); margin-top: 2px;
  }
  .contact {
    list-style: none;
    margin: 30px 0 0 120px;
    font-size: 16px; color: var(--grey-text);
    line-height: 1.5;
  }
  .contact b {
    color: var(--blue);
    font-family: "Exo 2", Arial, sans-serif;
    margin-right: 8px;
  }
  .address {
    position: absolute; left: 390px; bottom: 40px;
    font-size: 15px; color: var(--grey-text);
  }
</style>
</head>
<body>
<main class="sheet">

  <section class="card card-back" aria-label="Card back">
    <div class="card-back__band">
      <div class="wordmark"><span class="wordmark__dot"></span>Birch Hollow Dental</div>
    </div>
    <div class="appointment-lines">
      <span></span><span></span><span></span>
    </div>
  </section>

  <section class="card card-front" aria-label="Card front">
    <div class="card-front__photo" role="img" aria-label="Close-up photograph of a smiling mouth with bright white teeth"></div>
    <div class="card-front__info">
      <div class="wordmark"><span class="wordmark__dot"></span>Birch Hollow Dental</div>
      <div class="wordmark-rule"></div>
      <p class="doctor">Dr. Tomas K. Brellin DDS</p>
      <p class="specialty">Family and Cosmetic Dentistry</p>
      <ul class="contact">
        <li><b>T</b>518 642 7731</li>
        <li><b>F</b>518 642 7048</li>
      </ul>
    </div>
    <p class="address">4826 Delmore Rd., Schenectady NY 12417</p>
  </section>

</main>
</body>
</html>
```